AUDITING SERVICES FOR IMPORT/EXPORT/LOGISTICS

* PROCUREMENT OF PARTS / SERVICES
* BOAT POSITIONING

Industry/Entity Type

Auditing

Contact Information for Business Card

TRV CONSULTANTS
(TIDEWIND HULLCRAFT PTY LTD) 17 KESTREL VISTA CORALWOOD SHORES
DAVID HARTLEY 0417286342 JULIE-KATE HARTLEY 0417286918 (ON OPPOSITE SIDE)

```html
<!DOCTYPE html>
<html lang="en">
<head>
<meta charset="UTF-8">
<title>TRV Consultants — Business Card</title>
<link rel="stylesheet" href="https://fonts.googleapis.com/css2?family=Roboto:ital,wght@1,700;1,900&family=Roboto+Condensed:wght@700&display=swap">
<style>
  :root {
    --backdrop: #1b1b1c;
    --card: #2b2b2c;
    --accent: #29abe8;
    --ink: #ffffff;
  }
  html, body {
    margin: 0;
    padding: 0;
    width: 1200px;
    height: 800px;
    overflow: hidden;
    background: var(--backdrop);
  }
  .canvas {
    position: relative;
    width: 1200px;
    height: 800px;
  }
  .card {
    position: absolute;
    top: 268px;
    width: 478px;
    height: 288px;
    background: var(--card);
    box-shadow: 0 6px 18px rgba(0,0,0,0.45);
    color: var(--ink);
  }
  .card--front { left: 100px; }
  .card--back  { left: 623px; }

  /* Front */
  .brand {
    position: absolute;
    left: 0;
    right: 0;
    top: 112px;
    text-align: center;
  }
  .brand__name {
    display: block;
    font-family: "Roboto Condensed", "Arial Narrow", sans-serif;
    font-weight: 700;
    font-size: 40px;
    line-height: 1;
    letter-spacing: 0.5px;
    color: var(--accent);
  }
  .brand__legal {
    display: block;
    margin-top: 6px;
    font-family: "Roboto", Arial, sans-serif;
    font-style: italic;
    font-weight: 900;
    font-size: 14px;
    letter-spacing: 0.3px;
    color: var(--ink);
  }
  .services {
    position: absolute;
    left: 0;
    right: 0;
    top: 214px;
    margin: 0;
    padding: 0;
    list-style: none;
    text-align: center;
    font-family: "Roboto", Arial, sans-serif;
    font-style: italic;
    font-weight: 700;
    font-size: 13px;
    line-height: 16px;
    letter-spacing: 0.3px;
  }
  .services__item::before {
    content: "* ";
    color: var(--accent);
  }

  /* Back */
  .headline {
    position: absolute;
    left: 0;
    right: 0;
    top: 78px;
    text-align: center;
    font-family: "Roboto", Arial, sans-serif;
    font-style: italic;
    font-weight: 700;
  }
  .headline__intro {
    display: block;
    font-size: 12px;
    letter-spacing: 0.3px;
  }
  .headline__focus {
    display: block;
    font-weight: 900;
    font-size: 16px;
    letter-spacing: 0.4px;
    color: var(--accent);
  }
  .headline__slash { color: var(--ink); }
  .headline__rule {
    position: absolute;
    left: 117px;
    top: 111px;
  }
  .contacts {
    position: absolute;
    top: 162px;
    left: 0;
    width: 100%;
  }
  .contact {
    display: flex;
    align-items: baseline;
    height: 44px;
  }
  .contact__name {
    width: 252px;
    text-align: right;
    font-family: "Roboto", Arial, sans-serif;
    font-style: italic;
    font-weight: 900;
    font-size: 14px;
    letter-spacing: 0.3px;
    color: var(--accent);
  }
  .contact__phone {
    margin-left: 6px;
    font-family: "Roboto Condensed", "Arial Narrow", sans-serif;
    font-weight: 700;
    font-size: 29px;
    color: var(--ink);
  }
</style>
</head>
<body>
<main class="canvas">
  <section class="card card--front" aria-label="Business card front">
    <div class="brand">
      <span class="brand__name">TRV CONSULTANTS</span>
      <span class="brand__legal">TIDEWIND HULLCRAFT PTY LTD</span>
    </div>
    <ul class="services">
      <li class="services__item">Procurement of Parts / Services</li>
      <li class="services__item">Boat Positioning</li>
    </ul>
  </section>

  <section class="card card--back" aria-label="Business card back">
    <div class="headline">
      <span class="headline__intro">Auditing Services For</span>
      <span class="headline__focus">IMPORT<span class="headline__slash">/</span>EXPORT<span class="headline__slash">/</span>LOGISTICS</span>
    </div>
    <svg class="headline__rule" width="244" height="6" viewBox="0 0 244 6" aria-hidden="true">
      <polygon points="0,4 244,0 244,5 0,5" fill="#ffffff"/>
    </svg>
    <div class="contacts">
      <div class="contact">
        <span class="contact__name">DAVID HARTLEY</span>
        <span class="contact__phone">0417286342</span>
      </div>
      <div class="contact">
        <span class="contact__name">JULIE-KATE HARTLEY</span>
        <span class="contact__phone">0417286918</span>
      </div>
    </div>
  </section>
</main>
</body>
</html>
```